NEW Household Invention Needs a Package Design!

We need a 'retail' package design for a new product invented for the household kitchen market. Tiverlyn has developed a reusable food storage system that can be tailored to an individual's needs and have a sustainable impact on their ability to make good dietary decisions, while helping save the planet. We would like to see designs that use the brand's branding guidelines and logo. The final design should communicate the key features of the product (patented customizable modular system, fill lines, collapsible functionality and sustainable materials), as well as, all other notable aspects (Microwave/Dishwasher Safe, Leakproof, 100% BPA Free, Donates 1% of purchase price, etc.). It's important that the benefits of the product are well highlighted (More variety to better balance nutrition, More easily stored in bag, kitchen cabinet or drawer and Ends waste)
Updates

Hi All, we are looking for a package design for retail, something that will be on a shelf in our product category.

Need extra days to review

Target Market(s)

Health conscious men and women who have a passion for nutrition & social responsibility, operate a lifestyle on-the-go and monitor their spending by preparing meals at home.

Industry/Entity Type

Food Tech, Consumer Products, Health & Wellness

Font styles to use
Other font styles liked:
• See Brand Guidelines

Requirements
Must have
• Follow brand guidelines: https://guidelines.morbexcreative.com/tiverlyn/guidelines/

```html
<!DOCTYPE html>
<html lang="en">
<head>
<meta charset="utf-8">
<title>Tiverlyn Sleeve Designs</title>
<link href="https://fonts.googleapis.com/css2?family=Work+Sans:wght@400;500&display=swap" rel="stylesheet">
<style>
  :root {
    --sand: #e7d5b8;
    --sky: #a9dcf0;
    --coral: #f0564e;
    --plum: #8c1f62;
    --cream: #fbeef0;
    --ink: #4a1238;
  }
  * { margin: 0; padding: 0; box-sizing: border-box; }
  html, body { width: 1200px; height: 1150px; overflow: hidden; }
  body {
    position: relative;
    background: var(--sand);
    font-family: "Work Sans", Arial, sans-serif;
    font-weight: 400;
  }
  .panel, .dot, .photo, .lettering, .txt { position: absolute; }
  .sky { background: var(--sky); }
  .coral { background: var(--coral); }
  .plum { background: var(--plum); }
  .dot { border-radius: 50%; }
  .photo { border-radius: 50%; background: radial-gradient(circle at 40% 40%, #dff3fb, #6fb6d6 70%, #3b7d5a); }
  .photo.food { background: radial-gradient(circle at 45% 45%, #f3e27a, #9bcf7a 60%, #3c8a4b); }
  .photo.stack { background: radial-gradient(circle at 45% 40%, #ffffff, #c8e6f3 60%, #88bfd8); }
  .photo.globe { background: radial-gradient(circle at 45% 45%, #2f8a5a, #1f5f7a 65%, #c7e8f4); }
  .txt { line-height: 1.2; }
  .feature { font-size: 12px; color: var(--cream); }
  .feature.on-plum { color: var(--coral); }
  .brandname { font-weight: 500; letter-spacing: -0.5px; line-height: 1; }
  .specs { font-size: 5.6px; line-height: 1.35; }
  .cause { font-size: 5.6px; line-height: 1.35; color: var(--coral); }
  .cause b { font-weight: 400; font-size: 6.2px; }
  .benefit { font-size: 8.4px; line-height: 1.25; }
  .right { text-align: right; }
  .center { text-align: center; }
</style>
</head>
<body>

<!-- Sleeve one -->
<section class="sleeve sleeve-one">
  <div class="panel sky" style="left:89px;top:14px;width:92px;height:59px"></div>
  <div class="panel coral" style="left:181px;top:14px;width:181px;height:59px"></div>
  <div class="panel sky" style="left:89px;top:86px;width:92px;height:482px"></div>
  <div class="panel coral" style="left:181px;top:86px;width:181px;height:482px"></div>
  <div class="panel plum" style="left:89px;top:568px;width:92px;height:582px"></div>
  <div class="panel sky" style="left:181px;top:568px;width:181px;height:582px"></div>

  <p class="txt specs right" style="left:92px;top:159px;width:82px;color:var(--plum)">BPA Free &amp; Non Toxic<br>Lightweight &amp; Airtight<br>Microwave, Dishwasher, &amp;<br>Freezer Safe<br>Perfectly Portioned</p>
  <p class="txt brandname" style="left:184px;top:166px;font-size:34px;color:var(--plum)">Tiverlyn</p>

  <div class="photo" role="img" aria-label="Photo of modular container insert" style="left:126px;top:225px;width:52px;height:52px"></div>
  <p class="txt feature" style="left:187px;top:236px">Patented customizable<br>modular system</p>
  <div class="photo food" role="img" aria-label="Photo of filled meal container" style="left:126px;top:287px;width:52px;height:52px"></div>
  <p class="txt feature" style="left:187px;top:302px">Fill lines</p>
  <div class="photo stack" role="img" aria-label="Photo of collapsed containers" style="left:126px;top:349px;width:52px;height:52px"></div>
  <p class="txt feature" style="left:187px;top:366px">Collapsible&nbsp; functionality</p>
  <div class="photo globe" role="img" aria-label="Illustration of globe with produce" style="left:126px;top:407px;width:52px;height:52px"></div>
  <p class="txt feature" style="left:187px;top:425px">Sustainable materials</p>

  <p class="txt benefit right" style="left:92px;top:497px;width:83px;color:var(--plum)">Better Balance Nutrition, More Easily Store &amp; End Waste with Tiverlyn</p>
  <div class="lettering" role="img" aria-label="Hand lettering: For People &amp; Planet" style="left:190px;top:462px;width:162px;height:104px;background:var(--plum);border-radius:6px"></div>

  <p class="txt cause right" style="left:190px;top:584px;width:156px"><b>A container for a Cause</b><br>With every container sold, 1% of the purchase price will be donated to impact both people and planet.</p>
  <div class="dot sky" style="left:148px;top:635px;width:46px;height:46px"></div>
</section>

<!-- Sleeve two -->
<section class="sleeve sleeve-two">
  <div class="panel plum" style="left:463px;top:0;width:273px;height:78px"></div>
  <div class="panel plum" style="left:463px;top:84px;width:273px;height:484px"></div>
  <div class="panel sky" style="left:463px;top:568px;width:273px;height:582px"></div>

  <div class="dot coral" style="left:466px;top:86px;width:34px;height:34px"></div>

  <div class="photo" role="img" aria-label="Photo of modular container insert" style="left:519px;top:121px;width:56px;height:56px"></div>
  <p class="txt feature center" style="left:487px;top:179px;width:120px">Patented<br>customizable<br>modular system</p>
  <div class="photo food" role="img" aria-label="Photo of filled meal container" style="left:622px;top:121px;width:56px;height:56px"></div>
  <p class="txt feature center" style="left:590px;top:179px;width:120px">Fill lines</p>
  <div class="photo stack" role="img" aria-label="Photo of collapsed containers" style="left:519px;top:234px;width:56px;height:56px"></div>
  <p class="txt feature center" style="left:487px;top:296px;width:120px">Collapsible<br>functionality</p>
  <div class="photo globe" role="img" aria-label="Illustration of globe with produce" style="left:622px;top:234px;width:56px;height:56px"></div>
  <p class="txt feature center" style="left:590px;top:294px;width:120px">Sustainable<br>materials</p>

  <p class="txt brandname" style="left:477px;top:388px;font-size:62px;color:var(--coral)">Tiverlyn</p>

  <div class="lettering" role="img" aria-label="Hand lettering: For People &amp; Planet" style="left:480px;top:499px;width:102px;height:64px;background:var(--coral);border-radius:5px"></div>
  <p class="txt benefit right" style="left:612px;top:519px;width:95px;color:var(--cream)">Better Balance Nutrition, More Easily Store &amp; End Waste with Tiverlyn</p>

  <p class="txt specs right" style="left:580px;top:583px;width:127px;color:var(--ink)">BPA Free &amp; Non Toxic<br>Lightweight &amp; Airtight<br>Microwave, Dishwasher, &amp; Freezer Safe<br>Perfectly Portioned</p>
  <p class="txt cause right" style="left:580px;top:631px;width:127px"><b>A container for a Cause</b><br><span style="color:var(--ink)">With every container sold, 1% of the purchase price will be donated to impact both people and planet.</span></p>
  <div class="dot" style="left:502px;top:605px;width:44px;height:44px;background:#7cc9ea"></div>
  <div class="dot" style="left:648px;top:681px;width:46px;height:46px;background:#7cc9ea"></div>
</section>

<!-- Sleeve three -->
<section class="sleeve sleeve-three">
  <div class="panel coral" style="left:846px;top:24px;width:127px;height:64px"></div>
  <div class="panel plum" style="left:973px;top:24px;width:146px;height:64px"></div>
  <div class="panel coral" style="left:846px;top:100px;width:127px;height:483px"></div>
  <div class="panel plum" style="left:973px;top:100px;width:146px;height:483px"></div>
  <div class="panel plum" style="left:846px;top:583px;width:127px;height:158px;clip-path:polygon(0 0,100% 0,100% 93%,0 100%)"></div>
  <div class="panel sky" style="left:973px;top:583px;width:146px;height:158px;clip-path:polygon(0 0,100% 0,100% 88%,0 93%)"></div>
  <div class="panel plum" style="left:846px;top:730px;width:127px;height:420px;clip-path:polygon(0 18px,100% 10px,100% 100%,0 100%)"></div>
  <div class="panel sky" style="left:973px;top:722px;width:146px;height:428px;clip-path:polygon(0 18px,100% 8px,100% 100%,0 100%)"></div>

  <div class="photo" role="img" aria-label="Photo of modular container insert" style="left:908px;top:145px;width:56px;height:56px"></div>
  <p class="txt feature on-plum" style="left:977px;top:151px">Patented<br>customizable<br>modular system</p>
  <div class="photo food" role="img" aria-label="Photo of filled meal container" style="left:908px;top:214px;width:56px;height:56px"></div>
  <p class="txt feature on-plum" style="left:977px;top:236px">Fill lines</p>
  <div class="photo stack" role="img" aria-label="Photo of collapsed containers" style="left:908px;top:280px;width:56px;height:56px"></div>
  <p class="txt feature on-plum" style="left:977px;top:296px">Collapsible<br>functionality</p>
  <div class="photo globe" role="img" aria-label="Illustration of globe with produce" style="left:908px;top:345px;width:56px;height:56px"></div>
  <p class="txt feature on-plum" style="left:977px;top:363px">Sustainable<br>materials</p>

  <div class="lettering" role="img" aria-label="Hand lettering: For People &amp; Planet" style="left:862px;top:428px;width:104px;height:68px;background:var(--plum);border-radius:5px"></div>
  <div class="dot sky" style="left:855px;top:524px;width:46px;height:46px"></div>

  <p class="txt brandname" style="left:977px;top:515px;font-size:30px;color:var(--coral)">Tiverlyn</p>
  <p class="txt benefit" style="left:975px;top:551px;width:140px;color:var(--cream)">Better Balance Nutrition, More Easily Store &amp; End Waste with Tiverlyn</p>

  <div class="dot coral" style="left:899px;top:614px;width:46px;height:46px"></div>
  <p class="txt specs" style="left:984px;top:610px;width:130px;color:var(--ink)">BPA Free &amp; Non Toxic<br>Lightweight &amp; Airtight<br>Microwave, Dishwasher, &amp; Freezer Safe<br>Perfectly Portioned</p>
  <p class="txt cause" style="left:984px;top:663px;width:130px"><b>A container for a Cause</b><br>With every container sold, 1% of the purchase price will be donated to impact both people and planet.</p>
</section>

</body>
</html>
```